Carrow Equity Webinar Ads

Need a banner pack in less than 48 hours for this website:
http://carrowequity-example.com/webinar
Target Market(s)
Accredited real estate investors looking to grow their portfolio
Font styles to use
Sans Serif
Colors
0255a3
f37123
000000

```html
<!DOCTYPE html>
<html lang="en">
<head>
<meta charset="utf-8">
<title>Carrow Equity Webinar Ads</title>
<link rel="stylesheet" href="https://fonts.googleapis.com/css2?family=Ubuntu:wght@500;700&family=Questrial&family=Oswald:wght@500&display=swap">
<style>
  :root{
    --brand-blue:#0255a3;
    --brand-orange:#f37123;
    --brand-black:#000000;
    --headline-yellow:#f8c21c;
    --panel-deep:#062457;
    --panel-mid:#0c3f8c;
    --panel-light:#1a5cb4;
    --cta-dark:#111111;
    --cta-mid:#262626;
    --go-top:#ffd84a;
    --go-bottom:#f2a100;
    --white:#ffffff;
    --badge:#d7dee8;
    --stage-bg:#2b2520;
  }
  *{box-sizing:border-box;margin:0;padding:0}
  html,body{width:1200px;height:955px;overflow:hidden;background:var(--stage-bg)}
  .stage{position:relative;width:1052px;height:837px;transform:scale(1.1407);transform-origin:0 0}
  .banner{position:absolute;display:flex;overflow:hidden;background:var(--cta-dark);box-shadow:0 4px 10px rgba(0,0,0,.55)}
  .banner--row{flex-direction:row}
  .banner--col{flex-direction:column}

  /* brand area */
  .brand-area{background:var(--white);display:flex;align-items:center;justify-content:center;flex-shrink:0;gap:6px}
  .brand{display:flex;align-items:center;gap:4px}
  .brand-dot{display:block;border-radius:50%;background:var(--brand-blue);flex-shrink:0}
  .brand-name{font-family:"Ubuntu",sans-serif;font-weight:500;color:var(--brand-blue);white-space:nowrap}
  .listing-badge{display:block;background:var(--badge);border-radius:3px}

  /* message area */
  .message{position:relative;flex:1;display:flex;flex-direction:column;align-items:center;justify-content:center;text-align:center}
  .message-bg{position:absolute;inset:0;background:radial-gradient(ellipse at 50% 45%,var(--panel-light),var(--panel-mid) 55%,var(--panel-deep))}
  .message>*:not(.message-bg){position:relative}
  .headline{font-family:"Ubuntu",sans-serif;font-weight:500;color:var(--headline-yellow);line-height:1.12;text-shadow:0 1px 2px rgba(0,0,0,.6)}
  .body-copy{font-family:"Questrial",sans-serif;color:var(--white);text-transform:uppercase;line-height:1.15}
  .blueprint{font-family:"Ubuntu",sans-serif;font-weight:700;color:var(--white);text-transform:uppercase;line-height:1.15}

  /* call to action */
  .cta{background:linear-gradient(var(--cta-mid),var(--cta-dark));display:flex;align-items:center;justify-content:center;flex-shrink:0}
  .cta-label{font-family:"Oswald",sans-serif;font-weight:500;color:var(--brand-orange);text-transform:uppercase;line-height:1.05;text-align:center}
  .go{display:inline-flex;align-items:center;justify-content:center;gap:3px;border-radius:999px;background:linear-gradient(var(--go-top),var(--go-bottom));font-family:"Ubuntu",sans-serif;font-weight:700;color:var(--brand-black);border:1px solid #a86b00}
  .go svg{display:block}
</style>
</head>
<body>
<main class="stage">

  <!-- 728x90 -->
  <section class="banner banner--row" style="left:22px;top:18px;width:728px;height:90px">
    <div class="brand-area" style="width:160px;flex-direction:column;gap:8px">
      <div class="brand"><span class="brand-dot" style="width:14px;height:14px"></span><span class="brand-name" style="font-size:17px">Carrow Equity</span></div>
      <span class="listing-badge" style="width:80px;height:16px"></span>
    </div>
    <div class="message" style="gap:2px">
      <div class="message-bg" role="img" aria-label="Crowd of seminar attendees in blue tones"></div>
      <p class="headline" style="font-size:17px">Are You Maximizing Your Rental Portfolio Profits?</p>
      <p class="body-copy" style="font-size:15px">Discover how serious investors<br>are now doing just that…</p>
      <p class="blueprint" style="font-size:14px">6 Step Blueprint Revealed This Week</p>
    </div>
    <div class="cta" style="width:118px;flex-direction:column;gap:6px">
      <p class="cta-label" style="font-size:20px">Register for<br>the webinar</p>
      <span class="go" style="width:56px;height:20px;font-size:13px">GO<svg width="7" height="9" viewBox="0 0 7 9"><path d="M0 0L7 4.5L0 9Z" fill="#000"/></svg></span>
    </div>
  </section>

  <!-- 468x60 -->
  <section class="banner banner--row" style="left:22px;top:123px;width:468px;height:60px">
    <div class="brand-area" style="width:100px;flex-direction:column;gap:5px">
      <div class="brand"><span class="brand-dot" style="width:9px;height:9px"></span><span class="brand-name" style="font-size:11px">Carrow Equity</span></div>
      <span class="listing-badge" style="width:54px;height:11px"></span>
    </div>
    <div class="message" style="gap:1px">
      <div class="message-bg" role="img" aria-label="Crowd of seminar attendees in blue tones"></div>
      <p class="headline" style="font-size:11px">Are You Maximizing Your Rental Portfolio Profits?</p>
      <p class="body-copy" style="font-size:9.5px">Discover how serious investors<br>are now doing just that…</p>
      <p class="blueprint" style="font-size:9px">6 Step Blueprint Revealed This Week</p>
    </div>
    <div class="cta" style="width:78px;flex-direction:column;gap:3px">
      <p class="cta-label" style="font-size:13px">Register for<br>the webinar</p>
      <span class="go" style="width:36px;height:14px;font-size:9px">GO<svg width="5" height="7" viewBox="0 0 7 9"><path d="M0 0L7 4.5L0 9Z" fill="#000"/></svg></span>
    </div>
  </section>

  <!-- 160x600 -->
  <section class="banner banner--col" style="left:22px;top:198px;width:160px;height:600px">
    <div class="brand-area" style="height:118px;flex-direction:column;gap:14px">
      <span class="listing-badge" style="width:96px;height:20px"></span>
      <div class="brand"><span class="brand-dot" style="width:12px;height:12px"></span><span class="brand-name" style="font-size:17px">Carrow Equity</span></div>
    </div>
    <div class="message" style="gap:12px;padding:0 8px">
      <div class="message-bg" role="img" aria-label="Crowd of seminar attendees in blue tones"></div>
      <p class="headline" style="font-size:22px;line-height:1.3">Are You Maximizing Your Rental Portfolio Profits?</p>
      <p class="body-copy" style="font-size:17px;line-height:1.3">Discover how serious investors are now doing just that…</p>
      <p class="blueprint" style="font-size:14px;line-height:1.35">6 Step Blueprint Revealed This Week</p>
    </div>
    <div class="cta" style="height:115px;flex-direction:column;gap:12px">
      <p class="cta-label" style="font-size:24px">Register for<br>the webinar</p>
      <span class="go" style="width:80px;height:30px;font-size:18px">GO<svg width="9" height="12" viewBox="0 0 7 9"><path d="M0 0L7 4.5L0 9Z" fill="#000"/></svg></span>
    </div>
  </section>

  <!-- 120x600 -->
  <section class="banner banner--col" style="left:198px;top:198px;width:120px;height:600px">
    <div class="brand-area" style="height:100px;flex-direction:column;gap:14px">
      <span class="listing-badge" style="width:80px;height:18px"></span>
      <div class="brand"><span class="brand-dot" style="width:8px;height:8px"></span><span class="brand-name" style="font-size:12.5px">Carrow Equity</span></div>
    </div>
    <div class="message" style="gap:12px;padding:0 6px">
      <div class="message-bg" role="img" aria-label="Crowd of seminar attendees in blue tones"></div>
      <p class="headline" style="font-size:18px;line-height:1.3">Are You Maximizing Your Rental Portfolio Profits?</p>
      <p class="body-copy" style="font-size:14px;line-height:1.3">Discover how serious investors are now doing just that…</p>
      <p class="blueprint" style="font-size:14px;line-height:1.35">6 Step Blueprint Revealed This Week</p>
    </div>
    <div class="cta" style="height:115px;flex-direction:column;gap:12px">
      <p class="cta-label" style="font-size:21px">Register for<br>the webinar</p>
      <span class="go" style="width:80px;height:30px;font-size:18px">GO<svg width="9" height="12" viewBox="0 0 7 9"><path d="M0 0L7 4.5L0 9Z" fill="#000"/></svg></span>
    </div>
  </section>

  <!-- 336x280 -->
  <section class="banner banner--col" style="left:333px;top:198px;width:336px;height:280px">
    <div class="brand-area" style="height:57px;justify-content:space-around">
      <div class="brand"><span class="brand-dot" style="width:12px;height:12px"></span><span class="brand-name" style="font-size:16px">Carrow Equity</span></div>
      <span class="listing-badge" style="width:90px;height:20px"></span>
    </div>
    <div class="message" style="gap:6px">
      <div class="message-bg" role="img" aria-label="Crowd of seminar attendees in blue tones"></div>
      <p class="headline" style="font-size:24px">Are You Maximizing Your<br>Rental Portfolio Profits?</p>
      <p class="body-copy" style="font-size:21px;line-height:1.2">Discover how serious<br>investors are now<br>doing just that…</p>
      <p class="blueprint" style="font-size:13.5px">6 Step Blueprint Revealed This Week</p>
    </div>
    <div class="cta" style="height:38px;gap:10px">
      <p class="cta-label" style="font-size:21px">Register for the webinar</p>
      <span class="go" style="width:56px;height:22px;font-size:14px">GO<svg width="7" height="9" viewBox="0 0 7 9"><path d="M0 0L7 4.5L0 9Z" fill="#000"/></svg></span>
    </div>
  </section>

  <!-- 300x250 -->
  <section class="banner banner--col" style="left:684px;top:198px;width:300px;height:250px">
    <div class="brand-area" style="height:50px;justify-content:space-around">
      <div class="brand"><span class="brand-dot" style="width:10px;height:10px"></span><span class="brand-name" style="font-size:14px">Carrow Equity</span></div>
      <span class="listing-badge" style="width:78px;height:18px"></span>
    </div>
    <div class="message" style="gap:5px">
      <div class="message-bg" role="img" aria-label="Crowd of seminar attendees in blue tones"></div>
      <p class="headline" style="font-size:21px">Are You Maximizing Your<br>Rental Portfolio Profits?</p>
      <p class="body-copy" style="font-size:18px;line-height:1.2">Discover how serious<br>investors are now<br>doing just that…</p>
      <p class="blueprint" style="font-size:12px">6 Step Blueprint Revealed This Week</p>
    </div>
    <div class="cta" style="height:34px;gap:10px">
      <p class="cta-label" style="font-size:19px">Register for the webinar</p>
      <span class="go" style="width:50px;height:20px;font-size:13px">GO<svg width="7" height="9" viewBox="0 0 7 9"><path d="M0 0L7 4.5L0 9Z" fill="#000"/></svg></span>
    </div>
  </section>

  <!-- 250x250 -->
  <section class="banner banner--col" style="left:333px;top:493px;width:250px;height:250px">
    <div class="brand-area" style="height:50px;justify-content:space-around">
      <div class="brand"><span class="brand-dot" style="width:9px;height:9px"></span><span class="brand-name" style="font-size:12.5px">Carrow Equity</span></div>
      <span class="listing-badge" style="width:74px;height:17px"></span>
    </div>
    <div class="message" style="gap:5px">
      <div class="message-bg" role="img" aria-label="Crowd of seminar attendees in blue tones"></div>
      <p class="headline" style="font-size:17.5px">Are You Maximizing Your<br>Rental Portfolio Profits?</p>
      <p class="body-copy" style="font-size:18px;line-height:1.2">Discover how serious<br>investors are now<br>doing just that…</p>
      <p class="blueprint" style="font-size:10.5px">6 Step Blueprint Revealed This Week</p>
    </div>
    <div class="cta" style="height:34px;gap:10px">
      <p class="cta-label" style="font-size:16px">Register for the webinar</p>
      <span class="go" style="width:46px;height:18px;font-size:12px">GO<svg width="6" height="8" viewBox="0 0 7 9"><path d="M0 0L7 4.5L0 9Z" fill="#000"/></svg></span>
    </div>
  </section>

  <!-- 200x200 -->
  <section class="banner banner--col" style="left:598px;top:493px;width:200px;height:200px">
    <div class="brand-area" style="height:40px;justify-content:space-around">
      <div class="brand"><span class="brand-dot" style="width:8px;height:8px"></span><span class="brand-name" style="font-size:10.5px">Carrow Equity</span></div>
      <span class="listing-badge" style="width:58px;height:14px"></span>
    </div>
    <div class="message" style="gap:4px">
      <div class="message-bg" role="img" aria-label="Crowd of seminar attendees in blue tones"></div>
      <p class="headline" style="font-size:14px">Are You Maximizing Your<br>Rental Portfolio Profits?</p>
      <p class="body-copy" style="font-size:14.5px;line-height:1.2">Discover how serious<br>investors are now<br>doing just that…</p>
      <p class="blueprint" style="font-size:8.5px">6 Step Blueprint Revealed This Week</p>
    </div>
    <div class="cta" style="height:28px;gap:8px">
      <p class="cta-label" style="font-size:13px">Register for the webinar</p>
      <span class="go" style="width:38px;height:15px;font-size:10px">GO<svg width="5" height="7" viewBox="0 0 7 9"><path d="M0 0L7 4.5L0 9Z" fill="#000"/></svg></span>
    </div>
  </section>

</main>
</body>
</html>
```